Introduction:
We are an Australia-based Cyber Security Penetration testing company seeking a website redesign to showcase our services, expertise, and experience. Our target audience includes businesses and organizations of all sizes who are seeking to secure their IT infrastructure against cyber threats. The purpose of the website redesign is to increase our online presence, generate leads, and establish our company as a trusted authority in the industry.
Objectives:
Create a professional and modern website that is easy to navigate and user-friendly.
Provide information about our company, services, and expertise.
Clearly display table of our 3 services: Bug Bounty as a Service, Penetration Testing and Code Review.
Generate leads through online contact forms and calls-to-action.
Optimize the website for search engines to increase visibility and traffic.
Website similar to: https://www.velmoro.com.au/.
Target Audience:
Our target audience includes businesses and organizations of all sizes that require cybersecurity penetration testing services. These include:
Small and medium-sized enterprises (SMEs)
Australian Government agencies
Design Requirements:
Clean, modern, and professional design.
Use of colors that convey trust, reliability, and expertise (such as orange and grey).
Calls-to-action that encourage visitors to contact us or request a quote.
Integration with social media channels to increase engagement and brand awareness.
A blog section to showcase our thought leadership and expertise.
A news section to share updates about our company and the industry.
Content Requirements:
Home page that introduces our company and services and highlights our expertise.
About Us page that provides information about our company, team, and values.
Services page that lists our services and explains the benefits of each.
Case Studies page that showcases our previous work and success stories.
Contact Us page that includes a contact form, phone number, and email address.
Blog section with articles related to the cybersecurity industry and our services.
News section with updates about our company and the industry.

```html
<!DOCTYPE html>
<html lang="en">
<head>
<meta charset="utf-8">
<title>Emberhold – Penetration Testing</title>
<link rel="stylesheet" href="https://fonts.googleapis.com/css2?family=Montserrat:wght@400;500;600;700;800;900&display=swap">
<style>
:root{
  --orange:#ec7424;
  --orange-deep:#d9601a;
  --orange-light:#f59a4a;
  --ink:#1f1f1f;
  --text:#3a3a3a;
  --muted:#6b6b6b;
  --dark:#252628;
  --white:#ffffff;
}
*{box-sizing:border-box;margin:0;padding:0}
html,body{width:1200px;height:4843px;overflow:hidden}
body{font-family:"Montserrat",sans-serif;color:var(--text);background:var(--white);position:relative}
.abs{position:absolute}
section,header,footer{position:absolute;left:0;width:1200px}
.btn{position:absolute;display:flex;align-items:center;justify-content:space-between;background:var(--orange);color:#fff;font-weight:600;font-size:12px;border-radius:4px;padding:0 14px 0 18px}
.btn .ring{width:26px;height:26px;border:1.5px solid #fff;border-radius:50%;display:flex;align-items:center;justify-content:center}
.rule{position:absolute;height:2px;background:var(--orange);width:165px}
.rule::after{content:"";position:absolute;right:-3px;top:-3px;width:8px;height:8px;border-radius:50%;background:var(--orange)}
.photo{position:absolute}

/* header */
.site-header{top:0;height:96px;background:#fff}
.brand{position:absolute;left:113px;top:22px;display:flex;align-items:center;gap:10px}
.brand-mark{width:34px;height:34px;border-radius:50%;background:var(--orange)}
.brand-name{font-size:24px;font-weight:700;color:var(--orange)}
.nav{position:absolute;left:329px;top:40px;display:flex;gap:30px;font-size:11px;font-weight:600;color:var(--ink)}
.nav .active{color:var(--orange)}
.search{position:absolute;left:918px;top:36px}
.attack{position:absolute;left:957px;top:32px;width:130px;height:30px;background:var(--orange);color:#fff;font-size:12px;font-weight:500;border-radius:3px;display:flex;align-items:center;justify-content:center}

/* hero */
.hero{top:96px;height:654px}
.hero-photo{left:0;top:0;width:1200px;height:654px;background:linear-gradient(90deg,#7a4526 0%,#8a5532 30%,#3a3532 58%,#2a2c30 100%)}
.hero-fade{position:absolute;left:0;top:480px;width:1200px;height:174px;background:linear-gradient(180deg,rgba(255,255,255,0),#fff 70%)}
.hero-kicker{left:113px;top:160px;color:#fff;font-size:15px;font-weight:500}
.hero-title{left:113px;top:188px;color:#fff;font-size:54px;font-weight:900;line-height:60px;letter-spacing:1px}
.hero-sub{left:113px;top:340px;color:#fff;font-size:14px;font-weight:500}
.hero .btn{left:113px;top:397px;width:188px;height:47px}
.services-strip .item{position:absolute;top:524px;display:flex;gap:20px}
.svc-icon{width:72px;height:72px;border:3px solid var(--orange);border-radius:14px;background:#fff;display:flex;align-items:center;justify-content:center;flex-shrink:0}
.svc-title{font-size:17px;font-weight:500;color:var(--ink);margin-top:4px}
.svc-text{font-size:10px;line-height:14px;color:#333;width:200px;margin-top:6px}
.chevron{left:577px;top:736px}

/* chart */
.risks{top:800px;height:511px}
.risks-title{left:177px;top:27px;color:var(--orange);font-size:19px;font-weight:600}
.risks-chart{left:100px;top:0}
.risks-copy h2{position:absolute;left:641px;top:150px;font-size:26px;font-weight:700;color:var(--ink);line-height:31px;width:470px}
.risks-copy .rule{left:641px;top:223px;width:165px}
.risks-copy p{position:absolute;left:641px;top:249px;width:440px;font-size:12.5px;line-height:19.5px;color:#333}
.risks .btn{left:641px;top:372px;width:193px;height:47px}

/* clients */
.clients{top:1311px;height:248px;background:linear-gradient(180deg,#ea7a2c,#e56a1e);color:#fff}
.clients h2{position:absolute;width:1200px;top:50px;text-align:center;font-size:23px;font-weight:700}
.client-row{position:absolute;left:110px;top:120px;width:980px;display:flex;align-items:center;justify-content:space-between}
.client-name{font-size:34px;font-weight:700;color:#fff}
.arrow-lr{font-size:34px;font-weight:300}

/* different */
.different{top:1559px;height:807px}
.different-title{position:absolute;left:113px;top:148px;font-size:25px;font-weight:700;color:var(--ink)}
.different .rule{left:113px;top:195px}
.different-lead{position:absolute;left:113px;top:225px;width:400px;font-size:12.5px;line-height:19.5px}
.different .btn{left:113px;top:307px;width:192px;height:48px}
.diamond{left:637px;top:106px;width:246px;height:246px;transform:rotate(45deg);border-radius:30px;background:linear-gradient(135deg,#5a6470,#2d3339 60%,#1c2024);box-shadow:0 20px 40px rgba(0,0,0,.15)}
.feature{position:absolute;top:461px;width:226px;height:279px;background:#fff;box-shadow:0 4px 18px rgba(0,0,0,.1);text-align:center;padding:30px 16px 0}
.feature .ico{width:56px;height:56px;margin:0 auto;background:var(--orange);border-radius:10px;display:flex;align-items:center;justify-content:center}
.feature h3{font-size:15px;font-weight:600;color:var(--ink);margin:20px 0 10px}
.feature-text{font-size:11.5px;line-height:21px;color:#333}
.feature b{font-weight:600;color:var(--ink)}
.feature .hl{color:var(--orange)}

/* stats */
.stats{top:2366px;height:305px;background:linear-gradient(180deg,#ea7a2c,#e4691d);color:#fff;text-align:center}
.stat{position:absolute;top:70px;width:300px}
.stat .num{font-size:38px;font-weight:700;margin-top:20px}
.stat .lbl{font-size:13px;line-height:19px;margin-top:6px;font-weight:500}

/* news */
.news{top:2671px;height:668px}
.news h2{position:absolute;left:113px;top:62px;font-size:34px;font-weight:700;line-height:44px;color:var(--ink);width:480px}
.news h2 span{color:var(--orange)}
.news .lead{position:absolute;left:113px;top:200px;width:460px;font-size:12.5px;line-height:21px}
.news-photo{left:113px;top:310px;width:466px;height:288px;background:linear-gradient(135deg,#3a4550,#1f262c 60%,#3b3530)}
.latest-title{left:611px;top:65px;font-size:21px;font-weight:600;color:var(--ink)}
.news-item{position:absolute;width:224px}
.news-item .img{height:104px;background:linear-gradient(135deg,#4c5561,#1c2126)}
.news-item .date{font-size:9px;color:#555;margin-top:22px}
.news-item h4{font-size:14.5px;font-weight:600;line-height:19px;color:var(--ink);margin-top:8px}
.news-item .meta{display:flex;justify-content:space-between;font-size:9px;color:#333;margin-top:16px}
.news-item .meta span span{color:var(--orange)}

/* blogs */
.blogs{top:3339px;height:733px;background:linear-gradient(180deg,#e9782a,#e06a1f);color:#fff}
.blogs h2{position:absolute;width:1200px;top:63px;text-align:center;font-size:24px;font-weight:600}
.blogs .intro{position:absolute;width:1200px;top:112px;text-align:center;font-size:12.5px;line-height:22px}
.blogs .intro-rule{position:absolute;left:550px;top:163px;width:100px;height:1px;background:rgba(255,255,255,.7)}
.blog-card{position:absolute;top:197px;width:296px;height:446px;background:#fff;border-radius:12px;overflow:hidden;color:var(--ink)}
.blog-card .img{height:205px;background:linear-gradient(135deg,#5a6878,#232a30)}
.blog-card .body{padding:20px 16px}
.blog-card .date{font-size:9px;color:#555}
.blog-card h4{font-size:13px;font-weight:700;margin-top:12px}
.blog-card p{font-size:9.5px;line-height:16px;color:#555;margin-top:12px}
.blog-card .more{display:inline-block;margin-top:16px;background:var(--orange);color:#fff;font-size:11.5px;font-weight:600;padding:9px 14px;border-radius:3px}

/* team cta */
.team{top:4072px;height:316px;text-align:center}
.team h2{position:absolute;width:1200px;top:62px;font-size:41px;font-weight:900;line-height:47px;color:#111}
.team .cta{position:absolute;left:480px;top:188px;width:240px;height:62px;background:var(--orange);color:#fff;font-size:15px;font-weight:600;border-radius:4px;display:flex;align-items:center;justify-content:center}

/* footer */
.site-footer{top:4388px;height:455px;background:var(--dark);color:#fff}
.foot-brand{position:absolute;left:113px;top:70px;text-align:center}
.foot-brand .mark{width:54px;height:54px;border-radius:50%;background:#fff;margin:0 auto 10px}
.foot-brand .name{font-size:30px;font-weight:700}
.contact-row{position:absolute;left:113px;display:flex;gap:18px;align-items:flex-start;font-size:12px;line-height:16px}
.socials{position:absolute;left:113px;top:382px;display:flex;gap:24px}
.socials span{width:30px;height:30px;border:1.5px solid #fff;border-radius:50%}
.enquire h2{position:absolute;left:608px;top:68px;font-size:32px;font-weight:700;letter-spacing:1px}
.field{position:absolute;border:1.5px solid #fff;border-radius:3px;font-size:11px;padding:9px 10px}
.submit{position:absolute;left:609px;top:354px;width:132px;height:36px;border:1.5px solid var(--orange);border-radius:3px;font-size:12px;font-weight:700;display:flex;align-items:center;justify-content:center}
.copyright{position:absolute;left:0;top:427px;width:1200px;height:28px;background:var(--orange);font-size:11px;display:flex;align-items:center;justify-content:center}
</style>
</head>
<body>

<header class="site-header">
  <div class="brand"><span class="brand-mark"></span><span class="brand-name">Emberhold</span></div>
  <nav class="nav">
    <span class="active">HOME</span><span>ABOUT US</span><span>SERVICES</span><span>CASE STUDIES</span><span>CONTACT US</span><span>BLOG</span><span>NEWS</span>
  </nav>
  <svg class="search" width="22" height="22" viewBox="0 0 22 22"><circle cx="9" cy="9" r="6.5" fill="none" stroke="#ec7424" stroke-width="2"/><line x1="14" y1="14" x2="19" y2="19" stroke="#ec7424" stroke-width="2"/></svg>
  <div class="attack">Under Attack?</div>
</header>

<section class="hero">
  <div class="photo hero-photo" role="img" aria-label="Security engineer working at a computer with code on screen"></div>
  <div class="hero-fade"></div>
  <div class="abs hero-kicker"># Cyber Securiuty Experts</div>
  <h1 class="abs hero-title">PENETRATION<br>TESTING</h1>
  <p class="abs hero-sub">We offer a comprehensive suite of penetration testing services.</p>
  <div class="btn">Talk to Us Today <span class="ring"><svg width="14" height="10" viewBox="0 0 14 10"><path d="M0 5h12M8 1l4 4-4 4" fill="none" stroke="#fff" stroke-width="1.5"/></svg></span></div>
  <div class="services-strip">
    <div class="item" style="left:120px">
      <div class="svc-icon"><svg width="34" height="30" viewBox="0 0 34 30"><rect x="1" y="1" width="32" height="21" rx="2" fill="#222"/><path d="M13 8l-4 4 4 4M21 8l4 4-4 4M18 7l-2 10" stroke="#fff" stroke-width="1.6" fill="none"/><rect x="13" y="24" width="8" height="4" fill="#222"/></svg></div>
      <div><div class="svc-title">Incident Response</div><div class="svc-text"><b>Early detection</b> and a <b>swift response</b> are key. Our <b>cyber security consultants</b> lead from the front.</div></div>
    </div>
    <div class="item" style="left:468px">
      <div class="svc-icon"><svg width="30" height="32" viewBox="0 0 30 32"><rect x="2" y="2" width="22" height="28" rx="2" fill="#222"/><path d="M6 9h4M6 16h4M6 23h4M13 9h8M13 16h8M13 23h6" stroke="#fff" stroke-width="1.6"/></svg></div>
      <div><div class="svc-title">Governance &amp; Audit</div><div class="svc-text">Best-in-class <b>governance consultancy</b> and <b>information security services</b> for audit requirements.</div></div>
    </div>
    <div class="item" style="left:800px">
      <div class="svc-icon"><svg width="28" height="32" viewBox="0 0 28 32"><path d="M14 1l12 5v9c0 8-5 13-12 16C7 28 2 23 2 15V6z" fill="#222"/><path d="M14 6v20C9 24 7 20 7 15V9z" fill="#fff"/></svg></div>
      <div><div class="svc-title">Penetration Testing</div><div class="svc-text"><b>Robust</b> penetration testing services to validate your <b>defences</b> against modern, sophisticated attack methods.</div></div>
    </div>
  </div>
</section>
<svg class="abs chevron" style="top:732px" width="46" height="28" viewBox="0 0 46 28"><path d="M4 5l19 18L42 5" fill="none" stroke="#111" stroke-width="5" stroke-linecap="round"/></svg>

<section class="risks">
  <div class="abs risks-title">The Top Enterprise Cyber Risks for 2022 (%)</div>
  <svg class="abs risks-chart" width="520" height="480" viewBox="100 0 520 480">
    <defs><linearGradient id="bar" x1="0" y1="0" x2="0" y2="1"><stop offset="0" stop-color="#f07f2c"/><stop offset="1" stop-color="#ec7424"/></linearGradient></defs>
    <g font-family="Montserrat, sans-serif" font-size="12" font-weight="600" fill="#222">
      <text x="112" y="75">70</text><text x="112" y="127">60</text><text x="112" y="179">50</text><text x="112" y="231">40</text><text x="112" y="283">30</text><text x="112" y="335">20</text><text x="112" y="387">10</text><text x="112" y="438">0</text>
    </g>
    <rect x="186" y="330" width="32" height="104" fill="url(#bar)"/>
    <rect x="258" y="278" width="31" height="156" fill="url(#bar)"/>
    <rect x="331" y="71" width="32" height="363" fill="url(#bar)"/>
    <rect x="404" y="174" width="32" height="260" fill="url(#bar)"/>
    <rect x="474" y="226" width="32" height="208" fill="url(#bar)"/>
    <rect x="546" y="122" width="31" height="312" fill="url(#bar)"/>
    <g font-family="Montserrat, sans-serif" font-size="7" fill="#444" text-anchor="middle">
      <text x="202" y="448">Lorem ipsum</text><text x="202" y="456">dolor sit amet,</text><text x="202" y="464">consectetur</text>
      <text x="273" y="448">Lorem ipsum</text><text x="273" y="456">dolor sit amet,</text><text x="273" y="464">consectetur</text>
      <text x="347" y="448">Lorem ipsum</text><text x="347" y="456">dolor sit amet,</text><text x="347" y="464">consectetur</text>
      <text x="420" y="448">Lorem ipsum</text><text x="420" y="456">dolor sit amet,</text><text x="420" y="464">consectetur</text>
      <text x="490" y="448">Lorem ipsum</text><text x="490" y="456">dolor sit amet,</text><text x="490" y="464">consectetur</text>
      <text x="561" y="448">Lorem ipsum</text><text x="561" y="456">dolor sit amet,</text><text x="561" y="464">consectetur</text>
    </g>
  </svg>
  <div class="risks-copy">
    <h2>Today’s Enterprise risks are constantly evolving. Evolve faster.</h2>
    <div class="rule"></div>
    <p>As a leading cyber security consulting company, we understand that key Enterprise cyber risks are <b>constantly changing.</b> From ransomware and cryptolocker virus to phishing scams and brute force/DDoS attacks, cyber threat actors are <b>consistently innovating</b> to meet their objectives.</p>
  </div>
  <div class="btn">Get Started Now <span class="ring"><svg width="14" height="10" viewBox="0 0 14 10"><path d="M0 5h12M8 1l4 4-4 4" fill="none" stroke="#fff" stroke-width="1.5"/></svg></span></div>
</section>

<section class="clients">
  <h2>Our Clients</h2>
  <div class="client-row">
    <span class="arrow-lr">‹</span>
    <span class="client-name">Larkfield</span>
    <span class="client-name">Tallowmere</span>
    <span class="client-name">Brightquay</span>
    <span class="client-name">Ostrava</span>
    <span class="arrow-lr">›</span>
  </div>
</section>

<section class="different">
  <h2 class="different-title">What makes us different</h2>
  <div class="rule"></div>
  <p class="different-lead">We partner deeply with clients to understand their needs, working closely and iteratively to provide robust, best-in-class security solutions</p>
  <div class="btn">About Emberhold <span class="ring"><svg width="14" height="10" viewBox="0 0 14 10"><path d="M0 5h12M8 1l4 4-4 4" fill="none" stroke="#fff" stroke-width="1.5"/></svg></span></div>
  <div class="photo diamond" role="img" aria-label="Team of analysts collaborating at workstations"></div>

  <div class="feature" style="left:113px">
    <div class="ico"><svg width="30" height="30" viewBox="0 0 30 30" fill="#fff"><circle cx="15" cy="10" r="5"/><path d="M5 27c0-6 4-10 10-10s10 4 10 10z"/><circle cx="23" cy="22" r="4" fill="#ec7424" stroke="#fff" stroke-width="1.5"/></svg></div>
    <h3>Experience</h3>
    <p class="feature-text">A <b>nationally recognised</b> cyber security company having completed hundreds of <span class="hl">data breach investigations</span> globally.</p>
  </div>
  <div class="feature" style="left:361px">
    <div class="ico"><svg width="30" height="30" viewBox="0 0 30 30"><circle cx="15" cy="15" r="12" fill="none" stroke="#fff" stroke-width="2.5"/><circle cx="15" cy="12" r="4" fill="#fff"/><path d="M8 23c1-4 4-6 7-6s6 2 7 6" fill="#fff"/></svg></div>
    <h3>Leadership</h3>
    <p class="feature-text">Our company leaders are at the <b>forefront of research</b> for cyber security in Australia, having built industry <span class="hl">partnerships</span> with Australia’s leading universities.</p>
  </div>
  <div class="feature" style="left:613px">
    <div class="ico"><svg width="30" height="30" viewBox="0 0 30 30" fill="#fff"><circle cx="15" cy="10" r="5"/><path d="M5 27c0-6 4-10 10-10s10 4 10 10z"/><circle cx="23" cy="22" r="4" fill="#ec7424" stroke="#fff" stroke-width="1.5"/></svg></div>
    <h3>Experience</h3>
    <p class="feature-text">A <b>nationally recognised</b> cyber security company having completed hundreds of <span class="hl">data breach investigations</span> globally.</p>
  </div>
  <div class="feature" style="left:861px">
    <div class="ico"><svg width="30" height="30" viewBox="0 0 30 30"><circle cx="13" cy="13" r="9" fill="none" stroke="#fff" stroke-width="2.5"/><line x1="20" y1="20" x2="27" y2="27" stroke="#fff" stroke-width="3"/><circle cx="13" cy="11" r="3" fill="#fff"/></svg></div>
    <h3>Market-leading talent</h3>
    <p class="feature-text">We <b>employ the best talent</b> to ensure any cyber event experienced by our clients is addressed quickly, effectively and by people at the peak in</p>
  </div>
</section>

<section class="stats">
  <div class="stat" style="left:128px">
    <svg width="60" height="46" viewBox="0 0 60 46" fill="#fff"><circle cx="30" cy="10" r="8"/><circle cx="13" cy="15" r="6"/><circle cx="47" cy="15" r="6"/><path d="M18 46c0-12 5-20 12-20s12 8 12 20z"/><path d="M2 44c0-9 4-15 11-15 3 0 5 1 6 3-2 4-3 8-3 12z"/><path d="M58 44c0-9-4-15-11-15-3 0-5 1-6 3 2 4 3 8 3 12z"/></svg>
    <div class="num">1,000+</div>
    <div class="lbl">Satisfied clients that vouch<br>for our services</div>
  </div>
  <div class="stat" style="left:450px">
    <svg width="46" height="48" viewBox="0 0 46 48"><path d="M23 2l19 7v14c0 12-8 20-19 23C12 43 4 35 4 23V9z" fill="none" stroke="#fff" stroke-width="3"/><path d="M23 12l10 4v8c0 6-4 10-10 12z" fill="#fff"/></svg>
    <div class="num">25+</div>
    <div class="lbl">Proprietary Security Services<br>ready to scale</div>
  </div>
  <div class="stat" style="left:771px">
    <svg width="56" height="48" viewBox="0 0 56 48" fill="#fff"><rect x="4" y="2" width="48" height="12" rx="3"/><circle cx="28" cy="34" r="12" fill="none" stroke="#fff" stroke-width="3"/><path d="M28 34l6-6" stroke="#fff" stroke-width="3"/></svg>
    <div class="num">96</div>
    <div class="lbl">Net Promoter Score</div>
  </div>
</section>

<section class="news">
  <h2>Most <span>Sensational</span> News of The Week</h2>
  <p class="lead">Lorem ipsum dolor sit amet, consectetur adipiscing elit, sed do eiusmod tempor incididunt ut labore et dolore magna aliqua. Quis ipsum suspendisse ultrices gravida. Risus commodo viverra maecenas accumsan lacus vel facilisis.</p>
  <div class="photo news-photo" role="img" aria-label="Engineers reviewing work together in a dim office"></div>
  <div class="abs latest-title">Latest News</div>

  <div class="news-item" style="left:612px;top:109px">
    <div class="img" role="img" aria-label="Abstract network of glowing connections"></div>
    <div class="date">10 Oct - 2022</div>
    <h4>Lorem ipsum dolor sit amet, consectetur adipiscing elit.</h4>
    <div class="meta"><span>By <span>Harper</span> and <span>Quinn</span></span><span>1 Year ago</span></div>
  </div>
  <div class="news-item" style="left:855px;top:109px">
    <div class="img" role="img" aria-label="City skyline at night with location markers"></div>
    <div class="date">10 Oct - 2022</div>
    <h4>Lorem ipsum dolor sit amet, consectetur adipiscing elit.</h4>
    <div class="meta"><span>By <span>Harper</span> and <span>Quinn</span></span><span>1 Year ago</span></div>
  </div>
  <div class="news-item" style="left:612px;top:363px">
    <div class="img" role="img" aria-label="Person in silhouette beside a digital interface"></div>
    <div class="date">10 Oct - 2022</div>
    <h4>Lorem ipsum dolor sit amet, consectetur adipiscing elit.</h4>
    <div class="meta"><span>By <span>Harper</span> and <span>Quinn</span></span><span>1 Year ago</span></div>
  </div>
  <div class="news-item" style="left:855px;top:363px">
    <div class="img" role="img" aria-label="Office workers at computers"></div>
    <div class="date">10 Oct - 2022</div>
    <h4>Lorem ipsum dolor sit amet, consectetur adipiscing elit.</h4>
    <div class="meta"><span>By <span>Harper</span> and <span>Quinn</span></span><span>1 Year ago</span></div>
  </div>
</section>

<section class="blogs">
  <h2>Our Blogs</h2>
  <p class="intro">Lorem ipsum dolor sit amet, consectetur adipiscing elit. Morbi nec nulla elit. Sed volutpat ex elit,<br>sed gravida leo dignissim in. Morbi suscipit massa at tortor semper mattis pharetra ac nunc.</p>
  <div class="intro-rule"></div>

  <div class="blog-card" style="left:124px">
    <div class="img" role="img" aria-label="Analyst looking at monitoring dashboards"></div>
    <div class="body"><div class="date">10 Oct - 2022</div><h4>Lorem ipsum dolor sit amet</h4>
    <p>Lorem ipsum dolor sit amet, consectetur adipiscing elit, sed do eiusmod tempor incididunt ut labore et dolore magna aliqua. Quis ipsum suspendisse ultrices gravida. Risus commodo viverra maecenas accumsan lacus vel facilisis.</p>
    <span class="more">READ MORE</span></div>
  </div>
  <div class="blog-card" style="left:452px">
    <div class="img" role="img" aria-label="Hands typing on a laptop keyboard"></div>
    <div class="body"><div class="date">10 Oct - 2022</div><h4>Lorem ipsum dolor sit amet</h4>
    <p>Lorem ipsum dolor sit amet, consectetur adipiscing elit, sed do eiusmod tempor incididunt ut labore et dolore magna aliqua. Quis ipsum suspendisse ultrices gravida. Risus commodo viverra maecenas accumsan lacus vel facilisis.</p>
    <span class="more">READ MORE</span></div>
  </div>
  <div class="blog-card" style="left:781px">
    <div class="img" role="img" aria-label="Colleagues meeting around a table with laptops"></div>
    <div class="body"><div class="date">10 Oct - 2022</div><h4>Lorem ipsum dolor sit amet</h4>
    <p>Lorem ipsum dolor sit amet, consectetur adipiscing elit, sed do eiusmod tempor incididunt ut labore et dolore magna aliqua. Quis ipsum suspendisse ultrices gravida. Risus commodo viverra maecenas accumsan lacus vel facilisis.</p>
    <span class="more">READ MORE</span></div>
  </div>
</section>

<section class="team">
  <h2>OUR TEAM IS READY TO ANSWER<br>YOUR QUERIES.</h2>
  <div class="cta">CONTACT US NOW</div>
</section>

<footer class="site-footer">
  <div class="foot-brand"><div class="mark"></div><div class="name">Emberhold</div></div>
  <div class="contact-row" style="top:194px">
    <svg width="30" height="34" viewBox="0 0 30 34"><path d="M15 2a10 10 0 0 1 10 10c0 8-10 18-10 18S5 20 5 12A10 10 0 0 1 15 2z" fill="none" stroke="#fff" stroke-width="2.5"/><circle cx="15" cy="12" r="4" fill="#fff"/></svg>
    <span>Lorem ipsum dolor sit amet,<br>consectetur adipiscing elit,<br>sed do eiusmod tempor</span>
  </div>
  <div class="contact-row" style="top:272px;align-items:center">
    <svg width="30" height="30" viewBox="0 0 30 30"><path d="M7 3l5 5-3 4c2 4 5 7 9 9l4-3 5 5-4 4C13 27 3 17 3 7z" fill="#fff"/></svg>
    <span>02 - 5550 - 1873</span>
  </div>
  <div class="contact-row" style="top:322px;align-items:center">
    <svg width="30" height="22" viewBox="0 0 30 22"><rect x="1" y="1" width="28" height="20" rx="2" fill="#fff"/><path d="M2 3l13 10L28 3" fill="none" stroke="#252628" stroke-width="2"/></svg>
    <span>hello@emberhold-security.example</span>
  </div>
  <div class="socials" aria-label="Social media links"><span></span><span></span><span></span><span></span></div>

  <div class="enquire">
    <h2>ENQUIRE NOW</h2>
    <div class="field" style="left:609px;top:130px;width:209px;height:36px">Your Name</div>
    <div class="field" style="left:831px;top:130px;width:209px;height:36px">Your Company</div>
    <div class="field" style="left:609px;top:177px;width:209px;height:36px">Your Email</div>
    <div class="field" style="left:831px;top:177px;width:209px;height:36px">Your Phone</div>
    <div class="field" style="left:609px;top:224px;width:431px;height:113px">Your Requirements</div>
    <div class="submit">SUBMIT</div>
  </div>
  <div class="copyright">© Copyright 2023 Emberhold security. All Right Reserved</div>
</footer>

</body>
</html>
```